We need Pickled Vegetables jars label Design

Hello Artists,

We are looking for a new well-designed label for our Pickled Vegetables jars.
- You are free to choose between 2 styles, Vintage or Joyful.
- The label must be easy to adapt to different legume, so we can change the color or image to adapt it to other product (see image example).
- "Made in Canada" and Flag of Canada must be well visible.
- You are free to choose the label size so it feet the size of the jar which is: Circumference of cylinder: 30cm / height: 19cm.
- Label must be square or rectangle.
- The information to fill the label are included in the attachment.

Note: We love creatively crazy ideas.

Target Market(s)

Canada

Industry/Entity Type

Food Production

Colors

Designer to choose colors to be used in the design.

Requirements
Must have
• The label must be on piece of paper in rectangle or square shape.
Nice to have
• Your creative touch.

```html
<!DOCTYPE html>
<html lang="en">
<head>
<meta charset="utf-8">
<title>Marovane Pitted Green Olive Labels</title>
<link href="https://fonts.googleapis.com/css2?family=Bebas+Neue&family=Oswald:wght@500&family=Montserrat:wght@500&family=Noto+Naskh+Arabic&display=swap" rel="stylesheet">
<style>
  :root{
    --bg:#d6d6d6;
    --label-edge:rgba(255,255,255,.75);
    --label-fill:rgba(255,255,255,.18);
    --panel:#2c2c2d;
    --gold:#c9b766;
    --white:#f4f2ea;
    --brand-red:#d23a3a;
    --fresh-red:#d8323a;
    --olive-pill:#aab24a;
    --orange-pill:#f0863a;
    --red-pill:#e03338;
    --table-bg:#f3f1ea;
    --table-line:#c9b766;
    --ink:#2a2a2a;
    --art-light:#8a8a8c;
    --art-dark:#3a3a3c;
  }
  *{box-sizing:border-box;margin:0;padding:0}
  html,body{width:1200px;height:900px;overflow:hidden}
  body{background:radial-gradient(ellipse at center,#e4e4e4 0%,var(--bg) 100%);position:relative}

  .label{position:absolute;top:303px;width:350px;height:360px;
    border:1px solid var(--label-edge);background:var(--label-fill)}
  .label--olive{left:47px}
  .label--orange{left:432px}
  .label--red{left:812px}

  .label__panel{position:absolute;left:6px;top:43px;width:336px;height:222px}
  .label__brand{position:absolute;left:50%;top:12px;transform:translateX(-50%);
    height:48px;background:var(--brand-red);color:var(--white);border-radius:18px;
    border:2px solid var(--white);
    padding:0 26px;font:32px/46px "Bebas Neue",sans-serif;letter-spacing:1px;white-space:nowrap}
  .label__title{position:absolute;top:86px;width:100%;text-align:center;color:var(--gold);
    font:36px/1 "Bebas Neue",sans-serif;letter-spacing:2.5px;font-weight:400}
  .label__subtitle{position:absolute;top:118px;width:100%;text-align:center;color:var(--white);
    font:500 13px/1 "Montserrat",sans-serif;letter-spacing:2px}
  .label__arabic{position:absolute;top:132px;width:100%;text-align:center;color:var(--white);
    font:9px/1.2 "Noto Naskh Arabic",serif}
  .label__art{position:absolute;top:148px;left:100px;width:132px;height:88px;border-radius:44px 44px 50% 50%;
    background:radial-gradient(ellipse at 55% 60%,var(--art-light) 0%,var(--art-dark) 70%,rgba(58,58,60,0) 100%)}
  .label__variety{position:absolute;top:166px;left:113px;width:114px;height:22px;border-radius:11px;
    color:var(--white);text-align:center;font:20px/23px "Bebas Neue",sans-serif;letter-spacing:3px}
  .label--olive .label__variety{background:var(--olive-pill)}
  .label--orange .label__variety{background:var(--orange-pill)}
  .label--red .label__variety{background:var(--red-pill)}
  .label__fresh{position:absolute;top:200px;left:32px;width:45px;height:45px;border-radius:50%;
    background:var(--fresh-red);border:2px solid var(--white)}

  .label__facts{position:absolute;top:278px;left:30px;width:288px;background:var(--table-bg);
    border:1px solid var(--table-line);font:500 10.5px/1 "Oswald",sans-serif;color:var(--ink)}
  .facts__row{display:flex;border-bottom:1px solid var(--table-line)}
  .facts__row:last-child{border-bottom:none}
  .facts__cell{padding:9px 6px 8px;white-space:nowrap}
  .facts__row--top .facts__cell:first-child{width:138px;border-right:1px solid var(--table-line)}
  .facts__row--bottom .facts__cell:first-child{width:110px;border-right:1px solid var(--table-line)}
  .facts__cell:last-child{flex:1;text-align:right}
</style>
</head>
<body>
<main class="label-row">
  <section class="label label--olive">
    <svg class="label__panel" viewBox="0 0 336 222"><polygon points="20,0 316,0 336,20 336,140 168,222 0,140 0,20" fill="var(--panel)"/></svg>
    <div class="label__brand">MAROVANE</div>
    <h1 class="label__title">PITTED GREEN OLIVE</h1>
    <p class="label__subtitle">OLIVE VERTE PITÉE</p>
    <p class="label__arabic" lang="ar">الزيتون الأخضر</p>
    <div class="label__art" role="img" aria-label="Line drawing of an olive branch with olives"></div>
    <div class="label__variety">PICKLES</div>
    <div class="label__fresh" role="img" aria-label="Fresh badge"></div>
    <div class="label__facts">
      <div class="facts__row facts__row--top"><span class="facts__cell">NET WEIGHT</span><span class="facts__cell">100%ORGANIC</span></div>
      <div class="facts__row facts__row--bottom"><span class="facts__cell">MADE IN CANADA</span><span class="facts__cell">REFREGRATE AFTER OPENING</span></div>
    </div>
  </section>
  <section class="label label--orange">
    <svg class="label__panel" viewBox="0 0 336 222"><polygon points="20,0 316,0 336,20 336,140 168,222 0,140 0,20" fill="var(--panel)"/></svg>
    <div class="label__brand">MAROVANE</div>
    <h1 class="label__title">PITTED GREEN OLIVE</h1>
    <p class="label__subtitle">OLIVE VERTE PITÉE</p>
    <p class="label__arabic" lang="ar">الزيتون الأخضر</p>
    <div class="label__art" role="img" aria-label="Line drawing of an olive branch with olives"></div>
    <div class="label__variety">PICKLES</div>
    <div class="label__fresh" role="img" aria-label="Fresh badge"></div>
    <div class="label__facts">
      <div class="facts__row facts__row--top"><span class="facts__cell">NET WEIGHT</span><span class="facts__cell">100%ORGANIC</span></div>
      <div class="facts__row facts__row--bottom"><span class="facts__cell">MADE IN CANADA</span><span class="facts__cell">REFREGRATE AFTER OPENING</span></div>
    </div>
  </section>
  <section class="label label--red">
    <svg class="label__panel" viewBox="0 0 336 222"><polygon points="20,0 316,0 336,20 336,140 168,222 0,140 0,20" fill="var(--panel)"/></svg>
    <div class="label__brand">MAROVANE</div>
    <h1 class="label__title">PITTED GREEN OLIVE</h1>
    <p class="label__subtitle">OLIVE VERTE PITÉE</p>
    <p class="label__arabic" lang="ar">الزيتون الأخضر</p>
    <div class="label__art" role="img" aria-label="Line drawing of an olive branch with olives"></div>
    <div class="label__variety">PICKLES</div>
    <div class="label__fresh" role="img" aria-label="Fresh badge"></div>
    <div class="label__facts">
      <div class="facts__row facts__row--top"><span class="facts__cell">NET WEIGHT</span><span class="facts__cell">100%ORGANIC</span></div>
      <div class="facts__row facts__row--bottom"><span class="facts__cell">MADE IN CANADA</span><span class="facts__cell">REFREGRATE AFTER OPENING</span></div>
    </div>
  </section>
</main>
</body>
</html>
```